Tovrimel Complete Stationery - Logo already designed

I already have the logo designed see attached. I need have a full set of stationary and business card designed for printing. I have attached an example of what I mean.

Please feel free to be creative. Also you can use the X in the logo by its self if you think it will work.

My details:

Name: Dorian Pelsett
Social media handles: @dorianpelsett
W: dorianpelsett.com
E: info@dorianpelsett.com
​P: 08 7349 5286
PO Box 3872, Wendlemore 6047
ABN 83 274 908 615

Target Market(s)

Anyone looking to be inspired.

Industry/Entity Type

Business

Font styles to use
Sans Serif

Colors
fbee3e
000000

Requirements
Must have
• My details:
• Name: Dorian Pelsett
• Social media handles: @dorianpelsett
• W: dorianpelsett.com
• E: info@dorianpelsett.com
• ​P: 08 7349 5286
• PO Box 3872, Wendlemore 6047
• ABN 83 274 908 615
Nice to have
• Something a little different
Should not have
• must not look tacky.

```html
<!DOCTYPE html>
<html lang="en">
<head>
<meta charset="utf-8">
<title>Tovrimel Stationery</title>
<link rel="stylesheet" href="https://fonts.googleapis.com/css2?family=Arimo:wght@400;700&display=swap">
<style>
  :root {
    --bg: #e4e4e6;
    --paper: #ffffff;
    --ink: #000000;
    --text: #444444;
    --band: #231f20;
    --grey: #a3a4a6;
    --grey-light: #c9cacc;
    --yellow: #fbee3e;
    --blue: #2d6a9a;
    --on-band: #e8e8e8;
  }
  * { box-sizing: border-box; margin: 0; padding: 0; }
  html, body { width: 1200px; height: 1143px; overflow: hidden; }
  body { background: var(--bg); font-family: "Arimo", Arial, sans-serif; color: var(--text); position: relative; }
  .sheet { position: absolute; background: var(--paper); box-shadow: 0 2px 6px rgba(0,0,0,.12); overflow: hidden; }

  .brand { display: inline-flex; align-items: center; gap: 5px; font-weight: 700; color: var(--ink); letter-spacing: .5px; white-space: nowrap; }
  .brand-mark { background: var(--yellow); display: inline-block; }

  /* envelope */
  .envelope { left: 138px; top: 84px; width: 484px; height: 248px; background: #f2f2f3; }
  .envelope-flap { position: absolute; left: 0; top: 0; width: 100%; height: 97px; background: var(--grey); border-radius: 0 0 34px 34px; }
  .envelope-rule { position: absolute; left: 0; top: 214px; width: 100%; height: 4px; background: var(--grey-light); }
  .envelope-band { position: absolute; left: 0; top: 222px; width: 100%; height: 24px; background: var(--band); }

  /* notepad */
  .notepad { left: 686px; top: 150px; width: 290px; height: 190px; border-top: 5px solid var(--blue); padding: 20px; }
  .notepad-date { font-size: 28px; color: #333; margin-bottom: 10px; }
  .notepad-body { font-size: 7.5px; line-height: 1.55; color: #555; width: 230px; }

  /* letterhead */
  .letterhead { left: 138px; top: 385px; width: 457px; height: 669px; padding: 50px 32px 0; }
  .letterhead .brand { font-size: 34px; }
  .letterhead .brand-mark { width: 24px; height: 24px; }
  .letter { margin-top: 42px; font-size: 7.8px; line-height: 1.55; color: var(--text); }
  .letter p { margin-bottom: 14px; }
  .letter .date { margin-bottom: 12px; }
  .letter .salute { margin-bottom: 10px; }
  .letter .salute strong, .signer strong { color: #222; }
  .letter .gap { margin-bottom: 28px; }
  .signature { width: 58px; height: 30px; background: linear-gradient(90deg, #cfcfcf, #8a8a8a); margin: 6px 0; border-radius: 4px; }
  .letterhead-rule { position: absolute; left: 0; bottom: 28px; width: 100%; height: 4px; background: var(--grey); }
  .letterhead-band { position: absolute; left: 0; bottom: 0; width: 100%; height: 24px; background: var(--band);
    color: var(--on-band); font-size: 6.5px; line-height: 9px; padding: 3px 32px; text-align: center; }

  /* business cards */
  .card-front { left: 650px; top: 386px; width: 213px; height: 130px; }
  .card-back { left: 650px; top: 541px; width: 213px; height: 126px; }
  .card .brand { font-size: 17px; }
  .card .brand-mark { width: 11px; height: 11px; }
  .card-front .brand { position: absolute; left: 62px; top: 34px; }
  .card-front .card-name { position: absolute; left: 0; width: 100%; top: 60px; text-align: center; font-size: 7.5px; color: #333; }
  .card-back .brand { position: absolute; right: 16px; top: 28px; }
  .card-details { position: absolute; left: 18px; top: 14px; font-size: 6.2px; line-height: 9px; color: #333; }
  .card-details strong { font-size: 7px; color: #111; }
  .card-wave { position: absolute; left: 0; bottom: 0; width: 100%; }
  .card-tab { position: absolute; left: 0; top: 24px; width: 8px; height: 58px; background: var(--band); }

  /* id card */
  .id-card { left: 643px; top: 750px; width: 210px; height: 150px; border-top: 4px solid #2b2f3a; }
  .id-card .brand { position: absolute; left: 12px; top: 44px; font-size: 17px; }
  .id-card .brand-mark { width: 11px; height: 11px; }
  .id-bar { position: absolute; left: 0; top: 85px; width: 105px; height: 20px; background: var(--band); border-radius: 0 10px 10px 0;
    color: #fff; font-size: 8.5px; font-weight: 700; line-height: 20px; padding-left: 12px; white-space: nowrap; }
</style>
</head>
<body>

  <div class="sheet envelope">
    <div class="envelope-flap"></div>
    <div class="envelope-rule"></div>
    <div class="envelope-band"></div>
  </div>

  <div class="sheet notepad">
    <div class="notepad-date">11-07</div>
    <p class="notepad-body">is simply dummy text of the printing and typesetting industry. Lorem Ipsum has been the industry's standard dummy text ever since the 1500s, when an unknown printer took a galley of type and scrambled it to make a type specimen book. It has survived not only five centuries, but also the leap into electronic typesetting,remaining essentially unchanged.</p>
  </div>

  <div class="sheet letterhead">
    <div class="brand"><span>Tovrimel</span><span class="brand-mark"></span></div>
    <div class="letter">
      <p class="date">July 2, 2012</p>
      <p class="salute"><strong>Dear CH,</strong><br>ABC Building, def St., Country Name</p>
      <p>is simply dummy text of the printing and typesetting industry. Lorem Ipsum has been the industry's standard dummy text ever since the 1500s, when an unknown printer took a galley of type and scrambled it to make a type specimen book. It has survived not only five centuries, but also the leap into electronic typesetting, remaining essentially unchanged. It was popularised in the 1960s with the release of Pressline sheets containing Lorem Ipsum passages, and more recently with desktop publishing software like Corvel PageForm including versions of Lorem Ipsum.</p>
      <p class="gap">is simply dummy text of the printing and typesetting industry. Lorem Ipsum has been the industry's standard dummy text ever since the 1500s, when an unknown printer took a galley of type and scrambled it to make</p>
      <p>is simply dummy text of the printing and typesetting industry. Lorem Ipsum has been the industry's standard dummy text ever since the 1500s, when an unknown printer took a galley of type and scrambled it to make a type specimen book. It has survived not only five centuries, but also the leap into electronic typesetting, remaining essentially unchanged. It was popularised in the 1960s with the release of Pressline sheets containing Lorem Ipsum passages, and more recently with desktop publishing software like Corvel PageForm including versions of Lorem Ipsum.</p>
      <p style="margin-bottom:0">Best Regards,</p>
      <div class="signature" role="img" aria-label="Handwritten signature"></div>
      <p class="signer"><strong>Halden Voss</strong><br>Director<br><br>ABC Building, def St., Country Name</p>
    </div>
    <div class="letterhead-rule"></div>
    <div class="letterhead-band">
      Dorian Pelsett · P: 08 7349 5286 · E: info@dorianpelsett.com · W: dorianpelsett.com · @dorianpelsett<br>
      PO Box 3872, Wendlemore 6047 · ABN 83 274 908 615
    </div>
  </div>

  <div class="sheet card card-front">
    <div class="brand"><span>Tovrimel</span><span class="brand-mark"></span></div>
    <div class="card-name">Dorian Pelsett</div>
    <svg class="card-wave" width="213" height="34" viewBox="0 0 213 34" aria-hidden="true">
      <path d="M0 8 Q106 -6 213 8 L213 34 L0 34 Z" fill="#231f20"/>
    </svg>
  </div>

  <div class="sheet card card-back">
    <div class="card-tab"></div>
    <div class="card-details">
      <strong>Dorian Pelsett</strong><br>
      P: 08 7349 5286<br>
      E: info@dorianpelsett.com<br>
      W: dorianpelsett.com<br>
      @dorianpelsett<br>
      PO Box 3872, Wendlemore 6047<br>
      ABN 83 274 908 615
    </div>
    <div class="brand"><span>Tovrimel</span><span class="brand-mark"></span></div>
    <svg class="card-wave" width="213" height="46" viewBox="0 0 213 46" aria-hidden="true">
      <path d="M0 22 C50 12 90 38 140 28 C170 22 195 18 213 20 L213 46 L0 46 Z" fill="#a3a4a6"/>
      <path d="M0 30 C50 18 90 44 140 36 C170 30 195 28 213 30 L213 46 L0 46 Z" fill="#231f20"/>
    </svg>
  </div>

  <div class="sheet id-card">
    <div class="brand"><span>Tovrimel</span><span class="brand-mark"></span></div>
    <div class="id-bar">Dorian Pelsett</div>
  </div>

</body>
</html>
```